Freeze dried pet treats and chews packaging design

We are an Belgium based brand selling all natural treats and chews for pets. We are looking for a full color packaging design for a new line of freeze dried treats and chews for cats and dogs. The design should look familiar for our customers with our existing logo, but with a fresh new design especially for this new line. It should reflect our core values of natural, species appropriate food products without any additives or nasties.
The packaging will be a stand-up pouch with zipper, eurohole, easy open and with a window somewhere in the design to show the products inside. Please present your design as a mockup if possible.
Name of the product will be "Velmo Freeze Dried Bitzoos". Add icons to emphasize certain aspects of the product:
- 100% natural
- freeze dried (preserves all nutrients best)
- 100% mono protein
- without additives
- high in protein
- high in flavor
The design is a generic one for 12 different products, only one pouch will be produced and finished with 12 different round labels to indicate the protein source (beef, chicken, lamb, etc). You can include one of these stickers on your design to make the example complete. The sticker should have a separate color for every protein source to make it good distinguishable, an icon representing the protein source (see examples of existing packaging) and a round text around it with the protein source in text in Dutch, French and English (example: RUND - BŒUF - BEEF).
Important: after this design we need more designs for other new product lines, so the winner might get more out of this then only this one project!
High premium pet products
Petfood
- Fontastique, Roboto (used for logo and current designs), others welcome too

```html
<!DOCTYPE html>
<html lang="en">
<head>
<meta charset="utf-8">
<title>Velmo Freeze Dried Bitzoos – Pouch</title>
<link href="https://fonts.googleapis.com/css2?family=Montserrat:wght@800;900&family=Roboto:wght@500;700&display=swap" rel="stylesheet">
<style>
  :root {
    --backdrop: #c182fb;
    --pouch-dark: #3f1466;
    --pouch-mid: #5a2590;
    --pouch-light: #8a56bd;
    --white: #f4f1f7;
    --green: #8dbd3a;
    --green-light: #cfe3a6;
    --meat-dark: #6b5a55;
    --meat-light: #b4a69e;
  }
  * { margin: 0; padding: 0; box-sizing: border-box; }
  html, body { width: 1200px; height: 1200px; overflow: hidden; background: var(--backdrop); }
  .canvas { position: relative; width: 1200px; height: 1200px; }
  .pouch {
    position: absolute; left: 309px; top: 121px; width: 596px; height: 913px;
    border-radius: 22px 22px 6px 6px;
    background: linear-gradient(100deg, var(--pouch-dark) 0%, var(--pouch-mid) 45%, var(--pouch-light) 72%, var(--pouch-mid) 100%);
  }
  .brand-frame { position: absolute; left: 151px; top: 0; width: 288px; height: 316px; }
  .brand-name {
    position: absolute; left: 0; width: 100%; top: 165px; text-align: center;
    font-family: "Roboto", sans-serif; font-weight: 700; font-size: 56px; color: var(--white);
  }
  .brand-dot {
    position: absolute; left: 129px; top: 120px; width: 30px; height: 30px;
    border-radius: 50%; background: var(--green);
  }
  .hang-slot {
    position: absolute; left: 222px; top: 57px; width: 145px; height: 26px;
    border-radius: 13px; background: var(--pouch-light); opacity: .8;
  }
  .product-title {
    position: absolute; left: 0; width: 100%; top: 350px; text-align: center;
    font-family: "Montserrat", sans-serif; color: var(--white); line-height: 1;
  }
  .product-title .line-1 { display: block; font-weight: 800; font-size: 54px; letter-spacing: .5px; }
  .product-title .line-2 { display: block; font-weight: 900; font-size: 76px; margin-top: 8px; }
  .product-window {
    position: absolute; left: 170px; top: 512px; width: 268px; height: 268px; border-radius: 50%;
    border: 9px solid var(--green);
    background: radial-gradient(circle at 45% 40%, var(--meat-light), var(--meat-dark) 80%);
  }
  .protein-label { position: absolute; left: 373px; top: 505px; width: 104px; height: 104px; }
  .benefits {
    position: absolute; left: 90px; top: 830px; width: 460px;
    display: flex; justify-content: space-between;
  }
  .benefit { width: 86px; text-align: center; }
  .benefit svg { width: 52px; height: 52px; display: block; margin: 0 auto 6px; }
  .benefit span {
    display: block; font-family: "Roboto", sans-serif; font-weight: 500;
    font-size: 10.5px; line-height: 1.05; color: var(--white);
  }
</style>
</head>
<body>
<div class="canvas">
  <div class="pouch">
    <svg class="brand-frame" viewBox="0 0 288 316" aria-hidden="true">
      <path d="M2 0 V308 Q70 275 144 290 Q220 305 286 280 V0" fill="none" stroke="var(--white)" stroke-width="4"/>
    </svg>
    <div class="hang-slot"></div>
    <div class="brand-dot"></div>
    <div class="brand-name">Velmo</div>

    <h1 class="product-title">
      <span class="line-1">FREEZE DRIED</span>
      <span class="line-2">BITZOOS</span>
    </h1>

    <div class="product-window" role="img" aria-label="Window showing freeze dried beef chunks"></div>

    <svg class="protein-label" viewBox="0 0 104 104" aria-label="Protein label: beef">
      <defs><path id="ring" d="M52 52 m-38 0 a38 38 0 1 1 76 0 a38 38 0 1 1 -76 0"/></defs>
      <circle cx="52" cy="52" r="51" fill="var(--green-light)"/>
      <text font-family="Roboto, sans-serif" font-size="7.5" font-weight="500" fill="var(--white)" letter-spacing="1.2">
        <textPath href="#ring">RUND · BŒUF · BEEF · RUND · BŒUF · BEEF ·</textPath>
      </text>
      <circle cx="52" cy="52" r="24" fill="var(--white)" role="img" aria-label="Beef icon"/>
    </svg>

    <div class="benefits">
      <div class="benefit">
        <svg viewBox="0 0 52 52" aria-hidden="true"><circle cx="26" cy="26" r="23" fill="none" stroke="var(--white)" stroke-width="2"/><path d="M18 32 Q18 18 34 16 Q34 32 18 32 Z" fill="none" stroke="var(--white)" stroke-width="2"/></svg>
        <span>100% Natural</span>
      </div>
      <div class="benefit">
        <svg viewBox="0 0 52 52" aria-hidden="true"><circle cx="26" cy="26" r="23" fill="none" stroke="var(--white)" stroke-width="2"/><path d="M26 13 V39 M15 19.5 L37 32.5 M15 32.5 L37 19.5" stroke="var(--white)" stroke-width="2"/></svg>
        <span>Freeze Dried</span>
      </div>
      <div class="benefit">
        <svg viewBox="0 0 52 52" aria-hidden="true"><circle cx="26" cy="26" r="23" fill="none" stroke="var(--white)" stroke-width="2"/><path d="M18 36 L34 16 M18 16 L34 36" stroke="var(--white)" stroke-width="2"/><path d="M34 30 l4 4 l7 -8" fill="none" stroke="var(--white)" stroke-width="2"/></svg>
        <span>100% Mono Protein</span>
      </div>
      <div class="benefit">
        <svg viewBox="0 0 52 52" aria-hidden="true"><circle cx="26" cy="26" r="23" fill="none" stroke="var(--white)" stroke-width="2"/><path d="M10 10 L42 42" stroke="var(--white)" stroke-width="2"/><path d="M26 15 Q18 27 22 33 Q26 37 30 33 Q34 27 26 15 Z" fill="none" stroke="var(--white)" stroke-width="2"/></svg>
        <span>Without Additives</span>
      </div>
      <div class="benefit">
        <svg viewBox="0 0 52 52" aria-hidden="true"><circle cx="26" cy="26" r="23" fill="none" stroke="var(--white)" stroke-width="2"/><ellipse cx="31" cy="20" rx="6" ry="8" fill="none" stroke="var(--white)" stroke-width="2" transform="rotate(40 31 20)"/><path d="M27 25 L15 38" stroke="var(--white)" stroke-width="3"/></svg>
        <span>High In Flavor</span>
      </div>
    </div>
  </div>
</div>
</body>
</html>
```